New bussiness card, using company logo.
Lachlan Voss
Manager/Director
Birch Property Developments
Po Box 4657
Ashvale Central
Kld
0455 386 218
lachlan@birchpropertydevelopments
eye catching, vibrant colours, professional

```html
<!DOCTYPE html>
<html lang="en">
<head>
<meta charset="utf-8">
<title>Birch Property Developments – Business Card</title>
<link href="https://fonts.googleapis.com/css2?family=Source+Sans+3:wght@400;600;700&display=swap" rel="stylesheet">
<style>
  :root {
    --backdrop: #e4e4e4;
    --card-white: #ffffff;
    --card-fade: #f1f1f1;
    --slate: #6b6b6d;
    --slate-dark: #5c5c5e;
    --brand-red: #d8232a;
    --brand-green: #5cb646;
    --ink: #6a6a6a;
  }
  * { box-sizing: border-box; margin: 0; padding: 0; }
  html, body { width: 1200px; height: 800px; overflow: hidden; }
  body {
    background: var(--backdrop);
    font-family: "Source Sans 3", "Myriad Pro", Arial, sans-serif;
    position: relative;
  }
  .card {
    position: absolute;
    top: 248px;
    width: 520px;
    height: 297px;
    border-radius: 3px;
    overflow: hidden;
    box-shadow: 0 8px 24px rgba(0,0,0,.18);
  }

  /* Front */
  .card--front {
    left: 50px;
    background: linear-gradient(160deg, var(--card-white) 40%, var(--card-fade) 100%);
  }
  .front-band { position: absolute; left: 0; bottom: 0; width: 100%; height: 44px; }
  .front-wordmark {
    position: absolute; left: 34px; top: 36px;
    display: flex; align-items: center; gap: 10px;
    color: var(--brand-red); font-weight: 700; font-size: 22px; line-height: 1.05;
    letter-spacing: .2px;
  }
  .front-wordmark .mark-square { width: 14px; height: 14px; background: var(--brand-red); flex: none; }
  .contact-list { position: absolute; left: 34px; top: 124px; list-style: none; }
  .contact-list li {
    display: flex; align-items: center; gap: 8px;
    font-size: 13px; color: var(--ink); margin-bottom: 5px;
  }
  .contact-list svg { width: 12px; height: 12px; fill: var(--ink); flex: none; }
  .person { position: absolute; right: 34px; top: 114px; text-align: right; }
  .person__name { color: var(--brand-red); font-weight: 700; font-size: 19px; line-height: 1.1; }
  .person__role { color: var(--ink); font-size: 14px; }
  .postal {
    position: absolute; right: 34px; top: 166px; text-align: right;
    font-style: normal; color: var(--ink); font-size: 13px; line-height: 1.3;
  }

  /* Back */
  .card--back {
    left: 630px;
    background: linear-gradient(160deg, var(--slate) 0%, var(--slate-dark) 100%);
  }
  .back-url {
    position: absolute; left: 30px; top: 40px;
    color: var(--card-white); font-size: 13px; letter-spacing: .2px;
  }
  .back-wordmark {
    position: absolute; right: 30px; bottom: 38px;
    display: flex; align-items: center; gap: 10px;
    color: var(--card-white); font-weight: 700; font-size: 20px; line-height: 1.05; text-align: right;
  }
  .back-wordmark .mark-square { width: 12px; height: 12px; background: var(--card-white); flex: none; }
</style>
</head>
<body>

<section class="card card--front" aria-label="Business card front">
  <div class="front-wordmark">
    <span class="mark-square"></span>
    <span>Birch Property<br>Developments</span>
  </div>

  <ul class="contact-list">
    <li>
      <svg viewBox="0 0 12 12" aria-hidden="true"><rect x="3" y="0.5" width="6" height="11" rx="1"/><rect x="4" y="2" width="4" height="6" fill="#fff"/></svg>
      0455 386 218
    </li>
    <li>
      <svg viewBox="0 0 12 12" aria-hidden="true"><rect x="0.5" y="2.5" width="11" height="7"/><path d="M0.5 2.5 L6 7 L11.5 2.5" fill="none" stroke="#fff" stroke-width="1"/></svg>
      lachlan@birchpropertydevelopments
    </li>
  </ul>

  <div class="person">
    <p class="person__name">Lachlan Voss</p>
    <p class="person__role">Manager/Director</p>
  </div>

  <address class="postal">
    Birch Property Developments<br>
    Po Box 4657<br>
    Ashvale Central<br>
    Kld
  </address>

  <svg class="front-band" viewBox="0 0 520 44" preserveAspectRatio="none" aria-hidden="true">
    <polygon points="0,0 200,0 190,44 0,44" fill="var(--slate)"/>
    <polygon points="200,0 520,0 520,44 180,44" fill="var(--brand-green)"/>
  </svg>
</section>

<section class="card card--back" aria-label="Business card back">
  <p class="back-url">www.birchpropertydevelopments.com</p>
  <div class="back-wordmark">
    <span class="mark-square"></span>
    <span>Birch Property<br>Developments</span>
  </div>
</section>

</body>
</html>
```